Candy Bar Desgin

We need a postcard desgin for my new company. I just started a Candy bar/buffet called Sweet Table By Mimi. My motto is Sweet Table by Mimi for the teeny treaty. I will be attending a bridal show where I can display my work so there will be brides there. So I want something to pop. Maybe can add vases filled with candy. Add 20% off an event you book for attending the bridal show. I want colors. Candy colors. My company also do chocolate fountain bars as well. My website to add is www.sweettablebymimi.example
Email sweettablebymimi@mailbox.example
Phone 555-014-2968

Target Market(s)

Brides

Industry/Entity Type

It Company

Requirements
Must have
• Must have my motto. And my contact information
Should not have
• No old style don't like times new roman. Use fun fonts

```html
<!DOCTYPE html>
<html lang="en">
<head>
<meta charset="utf-8">
<title>Sweet Table by Mimi – Postcard</title>
<link rel="stylesheet" href="https://fonts.googleapis.com/css2?family=Lobster&family=Open+Sans&display=swap">
<style>
  :root {
    --page: #ffffff;
    --magenta: #d4208a;
    --teal: #3f9c93;
    --mint: #bfe8dc;
    --mint-light: #d8f1e9;
    --pink-soft: #f7c6dd;
    --pink-deep: #e47fb0;
    --jar-pink: #f2bcd3;
    --jar-mint: #b9e6df;
    --label: #222222;
  }
  * { margin: 0; padding: 0; box-sizing: border-box; }
  html, body { width: 848px; height: 1200px; overflow: hidden; background: var(--page); }
  body { position: relative; font-family: "Lobster", cursive; }

  .side-label {
    position: absolute;
    font-family: "Open Sans", sans-serif;
    font-size: 15px;
    color: var(--label);
  }
  .side-label--front { left: 162px; top: 108px; }
  .side-label--back { left: 155px; top: 1084px; }

  .card { position: absolute; overflow: hidden; }

  /* Front */
  .card--front { left: 153px; top: 162px; width: 540px; height: 417px; }
  .front-backdrop {
    position: absolute; inset: 0;
    background: linear-gradient(180deg,
      var(--pink-soft) 0%, #f4d4e4 10%,
      var(--mint) 16%, var(--mint-light) 75%,
      var(--pink-deep) 76%, #f2a9cb 90%, var(--pink-soft) 100%);
  }
  .front-candy-display {
    position: absolute; left: 31px; top: 127px; width: 502px; height: 240px;
    border-radius: 40px 40px 12px 12px;
    background:
      radial-gradient(ellipse 22% 45% at 14% 62%, var(--jar-pink) 0%, rgba(242,188,211,0.6) 60%, rgba(242,188,211,0) 100%),
      radial-gradient(ellipse 16% 48% at 40% 55%, #e9c9a6 0%, rgba(233,201,166,0.5) 60%, rgba(233,201,166,0) 100%),
      radial-gradient(ellipse 14% 40% at 66% 40%, #f5a9c8 0%, rgba(245,169,200,0.5) 60%, rgba(245,169,200,0) 100%),
      radial-gradient(ellipse 12% 55% at 88% 58%, var(--jar-mint) 0%, rgba(185,230,223,0.6) 60%, rgba(185,230,223,0) 100%),
      linear-gradient(180deg, rgba(255,255,255,0.35), rgba(255,255,255,0.15));
  }
  .front-title {
    position: absolute; right: 7px; top: 32px;
    text-align: right; color: var(--magenta); line-height: 1; font-weight: 400;
  }
  .front-title__name { font-size: 48px; display: block; }
  .front-title__motto { font-size: 32px; display: block; margin-top: 4px; }
  .front-offer {
    position: absolute; left: 0; right: 0; bottom: 4px;
    padding: 2px 9px;
    background: rgba(255,255,255,0.55);
    color: var(--teal);
    font-size: 25px; line-height: 1.25; white-space: nowrap;
  }

  /* Back */
  .card--back {
    left: 155px; top: 658px; width: 543px; height: 413px;
    border: 1.5px solid var(--magenta);
    background: var(--page);
    color: var(--magenta);
  }
  .back-title { position: absolute; left: 0; right: 0; top: 26px; text-align: center; font-size: 52px; line-height: 1; font-weight: 400; }
  .back-motto { position: absolute; right: 64px; top: 84px; font-size: 33px; line-height: 1; }
  .contact { position: absolute; left: 0; right: 0; text-align: center; line-height: 1; }
  .contact--web { top: 150px; font-size: 26px; }
  .contact--email { top: 218px; font-size: 28px; }
  .contact--phone { top: 293px; font-size: 35px; }
</style>
</head>
<body>
  <p class="side-label side-label--front">Front side</p>

  <section class="card card--front">
    <div class="front-backdrop" aria-hidden="true"></div>
    <div class="front-candy-display" role="img" aria-label="Candy buffet illustration: glass jars of pink jelly beans and heart cookies, a martini glass of candy canes and a tall jar of mints on a pink table"></div>
    <h1 class="front-title">
      <span class="front-title__name">Sweet Table by Mimi</span>
      <span class="front-title__motto">for the teeny treaty</span>
    </h1>
    <p class="front-offer">20% off an event you book attending the bridal show</p>
  </section>

  <section class="card card--back">
    <h2 class="back-title">Sweet Table by Mimi</h2>
    <p class="back-motto">for the teeny treaty</p>
    <p class="contact contact--web">www.sweettablebymimi.example</p>
    <p class="contact contact--email">email/sweettablebymimi@mailbox.example</p>
    <p class="contact contact--phone">phone/ 555 014 2968</p>
  </section>

  <p class="side-label side-label--back">Back</p>
</body>
</html>
```